Valmora Holdings - Tidal Crest Car Wash automatic car wash signage

We are wanting to have a new automatic car wash sign designed. Our current one is dated and there are numerous options that are no longer available. We like the look of a clean sharp design in keeping with the Tidal Crest colours; orange and blues. The sign should have the Ultimate and Premium options, the "Tidal Crest" and Tidal Crest Car Wash designed in a clean, concise and cool manner.

Font styles to use
Sans Serif

Colors
f37122
3276b5
0255a3
34a7d8

Requirements
Must have
• This project must have the Ultimate and Premium options, the "bucket" and the Tidal Crest Car Wash title. The orange is a key colour with blues for water.

```html
<!DOCTYPE html>
<html lang="en">
<head>
<meta charset="utf-8">
<title>Tidal Crest Car Wash – Wash Menu Sign</title>
<link href="https://fonts.googleapis.com/css2?family=Poppins:wght@600;700&family=Rubik:wght@800&display=swap" rel="stylesheet">
<style>
  :root {
    --orange: #f37122;
    --blue-mid: #3276b5;
    --blue-dark: #0255a3;
    --blue-light: #34a7d8;
    --water-pale: #e6f3fb;
    --water-soft: #c5e3f4;
    --white: #ffffff;
    --backdrop: #3b3b3b;
  }
  * { margin: 0; padding: 0; box-sizing: border-box; }
  html, body { width: 706px; height: 1200px; overflow: hidden; }
  body {
    background: radial-gradient(ellipse at 50% 45%, #6e6e6e 0%, var(--backdrop) 70%);
    font-family: "Poppins", sans-serif;
    position: relative;
  }
  .sign {
    position: absolute;
    left: 23px; top: 440px;
    width: 660px; height: 320px;
    overflow: hidden;
    box-shadow: 0 8px 24px rgba(0,0,0,.45);
  }
  .sign__water {
    position: absolute; inset: 0;
    background:
      radial-gradient(circle at 96% 75%, var(--water-soft) 0%, transparent 30%),
      radial-gradient(circle at 3% 90%, var(--water-soft) 0%, transparent 25%),
      linear-gradient(180deg, var(--water-pale) 0%, #d9edf8 100%);
  }
  .sign__header {
    position: absolute; left: 0; top: 0;
    width: 660px; height: 83px;
    background: var(--orange);
  }
  .brand-badge {
    position: absolute; left: 33px; top: -7px;
    width: 112px; height: 112px;
    border-radius: 50%;
    background: var(--white);
    border: 2px solid var(--blue-light);
    display: flex; align-items: center; justify-content: center;
    text-align: center;
  }
  .brand-badge__name {
    font-family: "Poppins", sans-serif;
    font-weight: 700;
    font-size: 19px;
    line-height: 1.05;
    color: var(--orange);
    text-transform: lowercase;
  }
  .sign__title {
    position: absolute; left: 152px; top: 16px;
    font-family: "Rubik", sans-serif;
    font-weight: 800;
    font-size: 42px;
    letter-spacing: -0.5px;
    color: var(--white);
    white-space: nowrap;
    -webkit-text-stroke: 1.5px var(--blue-dark);
    text-shadow: 2px 2px 0 var(--blue-mid);
  }
  .plan {
    position: absolute; top: 69px; height: 28px;
    border-radius: 14px 0 0 14px;
    color: var(--white);
    font-weight: 700; font-size: 16px;
    display: flex; align-items: center;
    padding-left: 14px;
  }
  .plan--ultimate { left: 332px; width: 140px; background: var(--blue-light); }
  .plan--premium  { left: 474px; width: 140px; background: var(--blue-dark); border-radius: 0; padding-left: 8px; }
  .price {
    position: absolute; top: 64px;
    width: 38px; height: 38px; border-radius: 50%;
    background: var(--orange);
    border: 2px solid var(--white);
    color: var(--white);
    font-family: "Rubik", sans-serif; font-weight: 800; font-size: 16px;
    display: flex; align-items: center; justify-content: center;
    letter-spacing: -0.5px;
  }
  .price--ultimate { left: 493px - 0px; left: 491px; left: 440px; }
  .price--premium  { left: 579px; }
  .menu {
    position: absolute; left: 43px; top: 101px;
    width: 578px;
    list-style: none;
  }
  .menu__row {
    display: grid;
    grid-template-columns: 290px 141px 147px;
    height: 19px;
    margin-bottom: 1.8px;
  }
  .menu__label {
    background: var(--orange);
    color: var(--white);
    font-weight: 600; font-size: 11.5px;
    text-transform: uppercase;
    display: flex; align-items: center;
    padding-left: 16px;
    white-space: nowrap;
    border-radius: 3px 0 0 3px;
  }
  .menu__cell {
    background: var(--white);
    border: 1px solid var(--orange);
    border-left: none;
    display: flex; align-items: center; justify-content: center;
  }
  .menu__cell:last-child { border-radius: 0 3px 3px 0; }
  .tick { width: 17px; height: 13px; }
  .tick--ultimate path { stroke: var(--blue-light); }
  .tick--premium path { stroke: var(--blue-dark); }
  .tick path { fill: none; stroke-width: 3.2; stroke-linecap: round; stroke-linejoin: round; }
</style>
</head>
<body>
<svg width="0" height="0" style="position:absolute">
  <defs>
    <symbol id="tick" viewBox="0 0 20 15"><path d="M2.5 8 L7.5 12.5 L17.5 2.5"/></symbol>
  </defs>
</svg>

<main class="sign" aria-label="Tidal Crest Car Wash wash menu">
  <div class="sign__water" role="img" aria-label="Pale blue water background with bubbles and splashes"></div>
  <header class="sign__header"></header>

  <div class="brand-badge"><span class="brand-badge__name">tidal<br>crest</span></div>
  <h1 class="sign__title">Tidal Crest Car Wash</h1>

  <div class="plan plan--ultimate">ULTIMATE</div>
  <div class="price price--ultimate">$14</div>
  <div class="plan plan--premium">PREMIUM</div>
  <div class="price price--premium">$12</div>

  <ul class="menu">
    <li class="menu__row"><span class="menu__label">Windshield &amp; Front End Bug Wash</span><span class="menu__cell"><svg class="tick tick--ultimate"><use href="#tick"/></svg></span><span class="menu__cell"></span></li>
    <li class="menu__row"><span class="menu__label">Under Carriage &amp; Wheel Blaster</span><span class="menu__cell"><svg class="tick tick--ultimate"><use href="#tick"/></svg></span><span class="menu__cell"><svg class="tick tick--premium"><use href="#tick"/></svg></span></li>
    <li class="menu__row"><span class="menu__label">Extra Pass of High Pressure Wash</span><span class="menu__cell"><svg class="tick tick--ultimate"><use href="#tick"/></svg></span><span class="menu__cell"></span></li>
    <li class="menu__row"><span class="menu__label">Try Foam Conditioner / Cleaner</span><span class="menu__cell"><svg class="tick tick--ultimate"><use href="#tick"/></svg></span><span class="menu__cell"></span></li>
    <li class="menu__row"><span class="menu__label">Side Kick Dryers</span><span class="menu__cell"><svg class="tick tick--ultimate"><use href="#tick"/></svg></span><span class="menu__cell"><svg class="tick tick--premium"><use href="#tick"/></svg></span></li>
    <li class="menu__row"><span class="menu__label">Wax / Surface Protectant</span><span class="menu__cell"><svg class="tick tick--ultimate"><use href="#tick"/></svg></span><span class="menu__cell"></span></li>
    <li class="menu__row"><span class="menu__label">On Board Overhead Dryer</span><span class="menu__cell"><svg class="tick tick--ultimate"><use href="#tick"/></svg></span><span class="menu__cell"><svg class="tick tick--premium"><use href="#tick"/></svg></span></li>
    <li class="menu__row"><span class="menu__label">Two Passes of Pre-Soak</span><span class="menu__cell"><svg class="tick tick--ultimate"><use href="#tick"/></svg></span><span class="menu__cell"><svg class="tick tick--premium"><use href="#tick"/></svg></span></li>
    <li class="menu__row"><span class="menu__label">High Pressure Wash Pass</span><span class="menu__cell"><svg class="tick tick--ultimate"><use href="#tick"/></svg></span><span class="menu__cell"><svg class="tick tick--premium"><use href="#tick"/></svg></span></li>
    <li class="menu__row"><span class="menu__label">Spot Free Rimse</span><span class="menu__cell"><svg class="tick tick--ultimate"><use href="#tick"/></svg></span><span class="menu__cell"><svg class="tick tick--premium"><use href="#tick"/></svg></span></li>
  </ul>
</main>
</body>
</html>
```